Event Poster for Bar Sunday Live Music and Happy Hour

We are a bar. Every Sunday we have a HARBOUR HOURS event where we have live music and a Sunday Happy Hour. I would like a poster that promotes this weekly event in A4 and A3. Information the poster should include:Event Name: SUNDAY SESSIONSVenue: Copper Lantern 218-222 Wattle Rd PrestonDrink Specials: 3:00 pm - 5:00pmLive Music: 4:30pm -6:30pmAttached is our logo.

Target Market(s)

Both sexes 30-40 year olds

Industry/Entity Type

Hospitality

Font styles to use
Sans Serif

Colors

Designer to choose colors to be used in the design.

Requirements
Must have
• Event Name: HARBOUR HOURS
• Venue: Copper Lantern 218-222 Wattle Rd Kelpie Bay
• Drink Specials: 3:00 pm - 5:00pm
• Live Music: 4:30pm -6:30pm
• Logo
Nice to have
• Open to different styles and ideas. Like colour.
Should not have
• It should not be too blokey are over the top bar-like.

```html
<!DOCTYPE html>
<html lang="en">
<head>
<meta charset="utf-8">
<title>Harbour Hours – Copper Lantern</title>
<link rel="stylesheet" href="https://fonts.googleapis.com/css2?family=Montserrat:wght@400;500;600;700&display=swap">
<style>
  :root {
    --night: #1c1440;
    --deep: #2a2a66;
    --steel: #4d6e9c;
    --ice: #8fd3ff;
    --glow: #5cc6ff;
    --white: #ffffff;
    --sky-text: #6fb9e4;
    --muted: #a8a6c8;
    --fine: #544f86;
  }
  * { margin: 0; padding: 0; box-sizing: border-box; }
  html, body { width: 848px; height: 1200px; overflow: hidden; background: var(--night); }
  body { font-family: "Montserrat", Arial, sans-serif; }

  .poster {
    position: relative;
    width: 848px;
    height: 1200px;
    overflow: hidden;
    background: linear-gradient(180deg, #3c5c8e 0%, #34477e 30%, #2b2e6a 55%, #221a4c 78%, var(--night) 100%);
  }

  .backdrop {
    position: absolute;
    inset: 0;
    background:
      radial-gradient(circle at 690px 120px, rgba(255,240,235,0.85) 0, rgba(255,230,230,0.35) 45px, transparent 80px),
      radial-gradient(circle at 185px 55px, rgba(255,255,255,0.7) 0, rgba(255,255,255,0.2) 30px, transparent 55px),
      radial-gradient(circle at 75px 330px, rgba(200,190,220,0.35) 0, transparent 90px),
      radial-gradient(circle at 620px 40px, rgba(230,220,240,0.35) 0, transparent 90px),
      radial-gradient(circle at 740px 560px, rgba(180,150,200,0.25) 0, transparent 110px),
      radial-gradient(circle at 60px 120px, rgba(120,200,255,0.45) 0, transparent 140px),
      radial-gradient(ellipse at 430px 500px, rgba(80,150,220,0.35) 0, transparent 380px);
  }

  .ring {
    position: absolute;
    left: 185px;
    top: 291px;
    width: 484px;
    height: 484px;
    border-radius: 50%;
    background: radial-gradient(circle, #2a2763 0%, #28245c 70%, #2d3576 100%);
    border: 3px solid rgba(143,211,255,0.85);
    box-shadow: 0 0 18px 4px rgba(92,198,255,0.7), inset 0 0 22px 4px rgba(92,198,255,0.45);
  }

  .venue-mark {
    position: absolute;
    left: 0; right: 0;
    top: 222px;
    text-align: center;
    color: var(--white);
    font-weight: 600;
    font-size: 20px;
    letter-spacing: 4px;
    text-transform: uppercase;
  }

  .event-title {
    position: absolute;
    left: 0; right: 0;
    top: 362px;
    text-align: center;
    color: var(--white);
    font-weight: 700;
    font-size: 84px;
    line-height: 102px;
    letter-spacing: 1px;
  }

  .schedule {
    position: absolute;
    left: 0; right: 0;
    top: 583px;
    text-align: center;
    color: var(--white);
    font-weight: 700;
    font-size: 17px;
    line-height: 24px;
    letter-spacing: 0.3px;
  }

  .address-box {
    position: absolute;
    left: 175px;
    top: 905px;
    width: 503px;
    height: 82px;
    border: 2px solid rgba(255,255,255,0.85);
    display: flex;
    align-items: center;
    justify-content: center;
    color: var(--white);
    font-weight: 700;
    font-size: 21px;
  }

  .details {
    position: absolute;
    left: 0; right: 0;
    top: 1008px;
    text-align: center;
    color: var(--sky-text);
    font-weight: 500;
    font-size: 19px;
    letter-spacing: 0.5px;
  }
  .details .dot { margin: 0 10px; }

  .website {
    position: absolute;
    left: 0; right: 0;
    top: 1086px;
    text-align: center;
    color: var(--muted);
    font-size: 15px;
    letter-spacing: 0.5px;
  }

  .fine-print {
    position: absolute;
    left: 70px; right: 70px;
    top: 1134px;
    text-align: center;
    color: var(--fine);
    font-size: 10px;
    line-height: 17px;
    text-transform: uppercase;
  }
</style>
</head>
<body>
  <main class="poster">
    <div class="backdrop" role="img" aria-label="Blurred bokeh lights over faceted blue and violet geometric shapes"></div>

    <div class="ring"></div>
    <div class="venue-mark">Copper Lantern</div>

    <h1 class="event-title">HARBOUR<br>HOURS</h1>

    <p class="schedule">KELPIE BAY DRINK SPECIALS: 3:00 PM - 5:00PM<br>LIVE MUSIC: 4:30PM -6:30PM</p>

    <div class="address-box">COPPER LANTERN 218 - 222 WATTLE RD</div>

    <p class="details">DOORS OPEN 22<span class="dot">•</span>$8 ENTRY<span class="dot">•</span>FREE PARKING</p>

    <p class="website">WWW.COPPERLANTERN.BAR</p>

    <p class="fine-print">Lorem ipsum dolor sit amet, consectetur adipiscing elit. Sed fermentum odio eget tellus lacinia, non placerat nulla facilisis. Etiam pulvinar, justo sed rhoncus iaculis, tortor nunc posuere massa, lobortis congue eros augue in erat.</p>
  </main>
</body>
</html>
```